Music Artist Needs Flyer Design ASAP

Looking for a flyer design to promote for artist release party. Music artist is mainly hip hop based. We would like designs that are simple, creative and eye catching.

Requirements
Must have
• The flyer must have the photo of the artist I attached incorporated into the design. Must say "Free ZuRK" Release Party, Live at Toller's Bar Thursday Dec.27 2012 (artist name=ZuRK VeNT), show starts at 8pm, No cover charge, 21 and over, Register to Win Borvale Comets tickets Giveaway

```html
<!DOCTYPE html>
<html lang="en">
<head>
<meta charset="utf-8">
<title>Free ZuRK Release Party</title>
<link rel="stylesheet" href="https://fonts.googleapis.com/css2?family=Rubik+Dirt&family=Permanent+Marker&family=Alfa+Slab+One&family=Black+Ops+One&family=Archivo+Black&display=swap">
<style>
  :root {
    --ink: #000000;
    --paper: #ffffff;
    --title-yellow: #f6ee1c;
    --band-yellow: #f8b532;
    --name-yellow: #f2e53a;
    --photo-glow: #f4d766;
    --photo-light: #e0aa2e;
    --photo-mid: #a86a14;
    --photo-dark: #2e1c06;
  }
  html, body { margin: 0; padding: 0; overflow: hidden; background: var(--ink); }
  .flyer {
    position: relative; width: 784px; height: 1200px; overflow: hidden;
    background: var(--ink); font-family: Arial, Helvetica, sans-serif;
  }
  .artist-photo {
    position: absolute; left: 55px; top: 177px; width: 669px; height: 690px;
    background:
      radial-gradient(ellipse 22% 16% at 52% 22%, rgba(214,160,90,0.95) 0%, rgba(214,160,90,0) 100%),
      radial-gradient(ellipse 34% 30% at 46% 52%, var(--photo-glow) 0%, rgba(244,215,102,0.6) 55%, rgba(244,215,102,0) 100%),
      radial-gradient(ellipse 26% 40% at 47% 82%, rgba(40,24,6,0.85) 0%, rgba(40,24,6,0) 100%),
      radial-gradient(ellipse 30% 25% at 85% 8%, rgba(250,200,60,0.9) 0%, rgba(250,200,60,0) 100%),
      radial-gradient(ellipse 20% 30% at 5% 45%, rgba(120,70,10,0.9) 0%, rgba(120,70,10,0) 100%),
      linear-gradient(180deg, var(--photo-light) 0%, var(--photo-mid) 45%, var(--photo-light) 70%, var(--photo-dark) 100%);
  }
  .event-title {
    position: absolute; left: 30px; top: 38px; width: 724px; margin: 0;
    text-align: center; font-family: 'Rubik Dirt', 'Permanent Marker', Impact, sans-serif;
    font-weight: 400; font-size: 124px; line-height: 1; color: var(--title-yellow);
    letter-spacing: 2px; white-space: nowrap;
  }
  .tag {
    position: absolute; background: var(--ink); color: var(--paper);
    font-family: 'Alfa Slab One', Georgia, serif; text-align: center; line-height: 1.08;
    box-sizing: border-box;
  }
  .tag-release { left: 55px; top: 180px; width: 247px; height: 132px; padding-top: 12px; }
  .tag-release .small { font-size: 42px; display: block; }
  .tag-release .big { font-size: 58px; display: block; }
  .tag-venue { left: 495px; top: 244px; width: 229px; height: 240px; padding-top: 6px; }
  .tag-venue .live { font-size: 56px; display: block; }
  .tag-venue .at { font-size: 46px; display: block; }
  .tag-venue .venue { font-size: 44px; display: block; }
  .tag-venue .bar { font-size: 42px; display: block; }
  .artist-name {
    position: absolute; left: 55px; top: 515px; width: 192px; height: 197px;
    background: var(--ink); color: var(--name-yellow); margin: 0;
    font-family: 'Black Ops One', Impact, sans-serif; font-weight: 400;
    font-size: 66px; line-height: 1.4; text-align: center; padding-top: 10px; box-sizing: border-box;
  }
  .date-badge {
    position: absolute; left: 484px; top: 508px; width: 256px; height: 256px;
    border-radius: 50%; background: var(--ink); color: var(--paper);
    text-align: center; font-weight: 700; box-sizing: border-box; padding-top: 46px;
  }
  .date-badge .day { font-size: 40px; display: block; line-height: 1.1; }
  .date-badge .month { font-size: 58px; line-height: 1; }
  .date-badge .num { font-size: 74px; line-height: 1; }
  .date-badge .year { font-size: 62px; display: block; line-height: 1.05; }
  .show-time {
    position: absolute; left: 0; top: 874px; width: 784px; margin: 0;
    text-align: center; color: var(--paper); font-size: 52px; font-weight: 700; line-height: 64px;
  }
  .info-band {
    position: absolute; left: 55px; top: 952px; width: 687px; height: 200px;
    background: var(--band-yellow);
  }
  .band-rule { position: absolute; left: 0; top: 68px; width: 687px; height: 7px; background: var(--ink); }
  .age-limit {
    position: absolute; left: 190px; top: 0; width: 497px; height: 68px;
    display: flex; align-items: center; gap: 6px;
    font-size: 56px; font-weight: 700; color: var(--ink); white-space: nowrap;
  }
  .age-limit::before, .age-limit::after {
    content: ""; flex: 1; height: 6px; background: var(--ink);
  }
  .giveaway {
    position: absolute; left: 200px; top: 84px; width: 487px; text-align: center;
    color: var(--ink); font-family: 'Archivo Black', 'Arial Black', sans-serif; line-height: 1.02;
  }
  .giveaway .lead { font-size: 30px; display: block; }
  .giveaway .team { font-size: 38px; display: block; }
  .giveaway .tail { font-size: 28px; display: block; }
  .cover-badge {
    position: absolute; left: 55px; top: 960px; width: 200px; height: 200px; border-radius: 50%;
    background: var(--ink); color: var(--paper); text-align: center; font-weight: 700;
    box-sizing: border-box; padding-top: 38px; line-height: 1;
  }
  .cover-badge .no { font-size: 48px; display: block; }
  .cover-badge .cover { font-size: 44px; display: block; }
  .cover-badge .charge { font-size: 38px; display: block; }
</style>
</head>
<body>
<main class="flyer">
  <div class="artist-photo" role="img" aria-label="Photo of the artist in a white tee with a chain, against a graffiti wall, in warm yellow tones"></div>
  <h1 class="event-title">Free ZuRK</h1>

  <div class="tag tag-release"><span class="small">Release</span><span class="big">Party</span></div>
  <div class="tag tag-venue"><span class="live">Live</span><span class="at">at</span><span class="venue">Toller's</span><span class="bar">BAR</span></div>

  <h2 class="artist-name">ZuRK<br>VeNT</h2>

  <div class="date-badge">
    <span class="day">Thursday</span>
    <span class="month">Dec</span><span class="num">27</span>
    <span class="year">2012</span>
  </div>

  <p class="show-time">SHOW STARTS AT 8pm</p>

  <section class="info-band">
    <div class="band-rule"></div>
    <div class="age-limit">21 and over</div>
    <div class="giveaway">
      <span class="lead">Register to Win</span>
      <span class="team">Borvale Comets</span>
      <span class="tail">tickets Giveaway</span>
    </div>
  </section>

  <div class="cover-badge"><span class="no">NO</span><span class="cover">cover</span><span class="charge">charge</span></div>
</main>
</body>
</html>
```